Tallow Bright business card

Tallow Bright is a new online life insurance company providing instant quotes and policies to consumers.
Target Market(s)
Target market is both business to business as well as business to consumer
Can think out side of the box- We are an open minded bunch
Industry/Entity Type
Life Insurance
Requirements
Must have
- Our corporate Logo
Double sided
Website www.tallowbright.com.au
Phone Number
Name & Position of each person etc.
Modern font

```html
<!DOCTYPE html>
<html lang="en">
<head>
<meta charset="utf-8">
<title>Tallow Bright business card</title>
<link href="https://fonts.googleapis.com/css2?family=Poppins:wght@400;500;600&display=swap" rel="stylesheet">
<style>
  :root {
    --ink: #2b2a29;
    --paper: #ffffff;
    --accent: #f28a1e;
    --backdrop: #e7e4df;
    --muted: #4a4947;
  }
  * { margin: 0; padding: 0; box-sizing: border-box; }
  html, body {
    width: 1200px; height: 900px; overflow: hidden;
    background: var(--backdrop);
    font-family: "Poppins", sans-serif;
  }
  .canvas { position: relative; width: 1200px; height: 900px; }
  .card {
    position: absolute; top: 297px;
    width: 530px; height: 306px;
    border-radius: 18px; overflow: hidden;
  }
  .card--front { left: 40px; background: var(--paper); color: var(--ink); }
  .card--back { left: 630px; background: var(--ink); color: var(--paper); }

  .brand-name { font-weight: 600; font-size: 44px; letter-spacing: -1px; line-height: 1; white-space: nowrap; }

  .card--front .brand { position: absolute; left: 38px; top: 44px; }

  .person { position: absolute; left: 38px; top: 168px; }
  .person-name { font-size: 21px; font-weight: 600; line-height: 1.1; }
  .person-role { font-size: 15px; color: var(--muted); }

  .contact { position: absolute; left: 38px; top: 234px; list-style: none; font-size: 12px; color: var(--muted); }
  .contact li { display: flex; align-items: center; gap: 8px; height: 18px; }
  .contact svg { width: 11px; height: 11px; fill: none; stroke: var(--accent); stroke-width: 2; }

  .card--back .brand { position: absolute; right: 60px; top: 98px; text-align: right; }
  .website { position: absolute; right: 60px; top: 212px; font-size: 15px; letter-spacing: 1px; }
</style>
</head>
<body>
<main class="canvas">
  <section class="card card--front">
    <div class="brand">
      <div class="brand-name">Tallow Bright</div>
    </div>
    <div class="person">
      <div class="person-name">Maren Holt</div>
      <div class="person-role">Director</div>
    </div>
    <ul class="contact">
      <li><svg viewBox="0 0 12 12"><path d="M2 2h3l1 3-1.5 1a6 6 0 0 0 2.5 2.5L8 7l3 1v3A9 9 0 0 1 1 2z"/></svg>844 500 37</li>
      <li><svg viewBox="0 0 12 12"><rect x="1" y="2.5" width="10" height="7"/><path d="M1 2.5l5 4 5-4"/></svg>maren@tallowbright.com.au</li>
      <li><svg viewBox="0 0 12 12"><circle cx="6" cy="6" r="5"/><path d="M1 6h10M6 1c-3 3-3 7 0 10M6 1c3 3 3 7 0 10"/></svg>tallowbright.com.au</li>
    </ul>
  </section>

  <section class="card card--back">
    <div class="brand">
      <div class="brand-name">Tallow Bright</div>
    </div>
    <div class="website">www.tallowbright.com.au</div>
  </section>
</main>
</body>
</html>
```